Web Design - Fitness for Middle Age Women

I need a web design for a start-up personal training company in Los Alamitos, CA called 'Maple Fitness & Health.' I would like to cater personal training services to middle-age mothers (30-50 years of age) who have kids and who would also want their children to receive services. The attached file is the logo of the company. Keep in mind the theme colors are white and blue and black, but make the background/pictures appealing to middle-age mothers. I want the flow of the website to be easy to use. The final design should present the company as a professional personal training service.

I realize this is a low budget project for designers but this is a budget I have to offer at the moment and if I take your design I will make sure to come back to improve the site when I'm able to gain more capital. I am looking for a full website built (using wordpress) with the following tabs (About / FAQ / Services / Clients / Location / Contact Us...and social media links to Chirper / Pictura / Circlebook)
Updates

I am looking over the current designs and narrowing down the decision. A decision will be made in the next 24-48 hours.

Target Market(s)

Middle-age mothers (30-55 years of age) who have children, an established career (or husband who is the bread-winner of the house) and has forgotten to take care of themselves and their body for years. I want them to realize lifestyle change is a choice, and it is a choice they need to make for themselves and their family to be a proper pattern for their children.

Industry/Entity Type

Fitness

Requirements
Must have
• The logo I have attached.

```html
<!DOCTYPE html>
<html lang="en">
<head>
<meta charset="utf-8">
<title>Maple Fitness &amp; Health</title>
<link href="https://fonts.googleapis.com/css2?family=Open+Sans:wght@400;600;700&family=Arimo:wght@400;700&display=swap" rel="stylesheet">
<style>
:root{
  --navy:#1f1856;
  --navy-dark:#17123f;
  --ink:#222;
  --muted:#a3a3a3;
  --rule:#e2e2e2;
  --card-bg:#f6f6f6;
  --band:#161616;
  --footer:#ececec;
  --white:#fff;
}
*{box-sizing:border-box;margin:0;padding:0}
html,body{width:1200px;height:2405px;overflow:hidden;background:var(--white)}
body{position:relative;font-family:"Open Sans",Arial,sans-serif;color:var(--ink)}
.abs{position:absolute}

/* hero */
.hero{left:0;top:0;width:1200px;height:690px;
  background:linear-gradient(180deg,#d6d9df 0%,#b9bec8 55%,#9ca3ae 86%,#2e3340 93%,#50565f 100%)}
.hero-card{left:155px;top:142px;width:353px;height:374px;background:var(--white);padding:24px 24px 0 24px}
.brand{display:flex;align-items:center;gap:12px;margin-left:10px}
.brand-dot{width:86px;height:86px;border-radius:50%;background:var(--navy);flex:none}
.brand-name{font-family:"Open Sans",sans-serif;font-weight:600;color:var(--navy);font-size:19px;line-height:1.15}
.hero-title{font-family:"Arimo",Arial,sans-serif;font-weight:700;color:var(--navy);font-size:25px;margin-top:20px}
.hero-text{font-family:"Arimo",Arial,sans-serif;font-size:13.5px;line-height:1.6;color:#333;margin-top:10px}
.btn{left:64px;top:298px;width:203px;height:46px;border-radius:9px;background:var(--navy);color:var(--white);
  font-family:"Arimo",Arial,sans-serif;font-size:25px;display:flex;align-items:center;justify-content:center}

/* nav */
.nav{left:0;top:690px;width:1200px;height:94px;border-bottom:2px solid var(--rule);
  display:flex;justify-content:center;align-items:center;gap:50px}
.nav a{font-family:"Arimo",Arial,sans-serif;font-weight:700;font-size:18px;color:#111;text-decoration:none;display:flex;align-items:center;gap:10px}
.nav svg{width:16px;height:16px;fill:var(--navy)}

/* features */
.feature{top:855px;width:372px;height:192px;background:var(--card-bg);border-bottom:4px solid var(--navy);padding:18px 20px}
.feature.active{background:var(--navy)}
.feature-head{display:flex;align-items:center;gap:14px;font-size:33px;color:#222}
.feature.active .feature-head,.feature.active p{color:var(--white)}
.feature-head svg{width:44px;height:44px}
.feature p{font-size:15px;line-height:1.6;color:var(--muted);margin-top:18px}
.connectors{left:0;top:1070px;width:1200px;height:180px}
.section-title{left:0;width:1200px;text-align:center}
.title-main{top:1232px;font-family:"Arimo",Arial,sans-serif;font-weight:700;font-size:36px;color:var(--navy)}
.title-sub{top:1288px;font-size:27px;color:var(--muted)}

/* programs */
.program{top:1443px;width:269px;height:236px;border:2px solid var(--rule);text-align:center;padding-top:96px}
.program-icon{left:50%;top:-64px;width:124px;height:124px;margin-left:-62px}
.program h3{font-weight:400;font-size:25px;color:#111}
.program p{font-size:15px;line-height:1.55;color:var(--muted);margin:22px 28px 0}

/* promo band */
.band{left:0;top:1740px;width:1200px;height:352px;background:var(--band)}
.band-photo{left:615px;top:0;width:585px;height:352px;
  background:linear-gradient(90deg,var(--band) 0%,#4a3c33 25%,#a0826c 50%,#c4a48a 65%,#8d9a6a 80%,#2b2b2b 100%)}
.band-line{font-weight:700;font-size:29px;color:#bdbdbd;letter-spacing:.5px}
.band-line b{color:var(--white)}
.band-rule{left:120px;top:2023px;width:374px;height:2px;background:#cfcfcf}
.band-note{left:88px;top:2046px;font-size:11px;color:var(--white);letter-spacing:.3px}

/* social */
.social-title{top:2130px;font-family:"Arimo",Arial,sans-serif;font-weight:700;font-size:36px;color:var(--navy)}
.social-sub{top:2182px;font-size:27px;color:var(--muted)}
.social{top:2259px;display:flex;align-items:center;gap:20px;font-family:"Arimo",Arial,sans-serif;font-size:18px;color:#333}
.social-mark{width:38px;height:38px;background:#555;border-radius:4px}

.footer{left:0;top:2325px;width:1200px;height:80px;background:var(--footer);display:flex;align-items:center;justify-content:center;font-size:13px;color:#9a9a9a}
</style>
</head>
<body>

<section class="abs hero" role="img" aria-label="Photo of a woman in white workout clothes stretching on a mat against a soft grey studio backdrop"></section>

<div class="abs hero-card">
  <div class="brand">
    <span class="brand-dot"></span>
    <span class="brand-name">Maple<br>Fitness &amp; Health</span>
  </div>
  <h1 class="hero-title">Your new personal trainer</h1>
  <p class="hero-text">Sed egestas, ante et vulputate volutpat, eros pede semper est, vitae luctus metus libero eu augue. Morbi purus libero, faucibus adipiscing, commodo quis, gravida id, est.</p>
  <a class="abs btn">Contact me</a>
</div>

<nav class="abs nav">
  <a><svg viewBox="0 0 16 16"><path d="M8 0l2.4 5.2 5.6.6-4.2 3.8 1.2 5.6L8 12.4 3 15.2l1.2-5.6L0 5.8l5.6-.6z"/></svg>About me</a>
  <a><svg viewBox="0 0 16 16"><rect x="0" y="1" width="3" height="3"/><rect x="5" y="1" width="11" height="3"/><rect x="0" y="6.5" width="3" height="3"/><rect x="5" y="6.5" width="11" height="3"/><rect x="0" y="12" width="3" height="3"/><rect x="5" y="12" width="11" height="3"/></svg>My program</a>
  <a><svg viewBox="0 0 16 16"><path d="M8 8V1a7 7 0 1 1-7 7z"/><path d="M9.5 0a6.5 6.5 0 0 1 6.5 6.5H9.5z"/></svg>Prices</a>
  <a><svg viewBox="0 0 16 16"><path d="M3 0h10v16l-5-4-5 4z"/></svg>Opinion</a>
  <a><svg viewBox="0 0 16 16"><path d="M2 0h12v16H2z"/><rect x="4" y="3" width="8" height="1.5" fill="#fff"/><rect x="4" y="7" width="8" height="1.5" fill="#fff"/><rect x="4" y="11" width="5" height="1.5" fill="#fff"/></svg>Blog</a>
  <a><svg viewBox="0 0 16 16"><path d="M8 0a5.5 5.5 0 0 1 5.5 5.5C13.5 10 8 16 8 16S2.5 10 2.5 5.5A5.5 5.5 0 0 1 8 0zm0 3a2.5 2.5 0 1 0 0 5 2.5 2.5 0 0 0 0-5z"/></svg>Contact me</a>
</nav>

<article class="abs feature" style="left:16px">
  <div class="feature-head"><svg viewBox="0 0 44 44" fill="none" stroke="#222" stroke-width="3"><circle cx="22" cy="22" r="19"/><path d="M10 22h24M16 15v14M28 15v14"/></svg>Fitness</div>
  <p>Praesent dapibus, neque id cursus fauci-bus, tortor neque egestas augue, eu vulpu-tate magna eros eu erat.</p>
</article>
<article class="abs feature active" style="left:414px">
  <div class="feature-head"><svg viewBox="0 0 44 44" fill="none" stroke="#fff" stroke-width="3"><path d="M10 4v12a4 4 0 0 0 8 0V4M14 4v38M30 4c-5 4-5 16 0 18v20"/></svg>Diet</div>
  <p>Praesent dapibus, neque id cursus fauci-bus, tortor neque egestas augue, eu vulpu-tate magna eros eu erat.</p>
</article>
<article class="abs feature" style="left:815px">
  <div class="feature-head"><svg viewBox="0 0 44 44" fill="none" stroke="#222" stroke-width="3"><rect x="6" y="3" width="32" height="38"/><circle cx="22" cy="17" r="5"/><path d="M13 32c2-6 16-6 18 0M2 10h4M2 22h4M2 34h4"/></svg>Habbits</div>
  <p>Praesent dapibus, neque id cursus fauci-bus, tortor neque egestas augue, eu vulpu-tate magna eros eu erat.</p>
</article>

<svg class="abs connectors" viewBox="0 0 1200 180">
  <g stroke="#cfcfcf" stroke-width="2">
    <line x1="176" y1="28" x2="598" y2="150"/>
    <line x1="1018" y1="28" x2="598" y2="150"/>
    <line x1="598" y1="28" x2="598" y2="150"/>
  </g>
  <g fill="#fff" stroke="#1f1856" stroke-width="3">
    <circle cx="176" cy="28" r="17"/><circle cx="598" cy="28" r="17"/><circle cx="1018" cy="28" r="17"/>
  </g>
  <g fill="#1f1856"><circle cx="176" cy="28" r="10"/><circle cx="598" cy="28" r="10"/><circle cx="1018" cy="28" r="10"/></g>
</svg>

<h2 class="abs section-title title-main">3 points which strike</h2>
<p class="abs section-title title-sub">to give you a new, perfect body</p>

<svg width="0" height="0" style="position:absolute">
  <symbol id="watch" viewBox="0 0 124 124">
    <circle cx="62" cy="62" r="62" fill="#1f1856"/>
    <circle cx="62" cy="62" r="47" fill="none" stroke="#fff" stroke-width="3"/>
    <rect x="52" y="36" width="20" height="52" rx="3" fill="#fff"/>
    <circle cx="62" cy="62" r="15" fill="#fff" stroke="#1f1856" stroke-width="3"/>
    <path d="M62 54v8h6" stroke="#1f1856" stroke-width="3" fill="none"/>
  </symbol>
</svg>
<article class="abs program" style="left:16px"><svg class="abs program-icon"><use href="#watch"/></svg><h3>PROGRAME ONE</h3><p>Praesent dapibus, neque id cursus faucibus, tortor neque egestas augue.</p></article>
<article class="abs program" style="left:315px"><svg class="abs program-icon"><use href="#watch"/></svg><h3>PROGRAME TWO</h3><p>Praesent dapibus, neque id cursus faucibus, tortor neque egestas augue.</p></article>
<article class="abs program" style="left:615px"><svg class="abs program-icon"><use href="#watch"/></svg><h3>PROGRAME THREE</h3><p>Praesent dapibus, neque id cursus faucibus, tortor neque egestas augue.</p></article>
<article class="abs program" style="left:914px"><svg class="abs program-icon"><use href="#watch"/></svg><h3>PROGRAME FOUR</h3><p>Praesent dapibus, neque id cursus faucibus, tortor neque egestas augue.</p></article>

<section class="abs band">
  <div class="abs band-photo" role="img" aria-label="Photo of a toned midriff with a woman lifting her light green top"></div>
</section>
<p class="abs band-line" style="left:123px;top:1806px"><b>ONLINE</b> CONSULTATION</p>
<p class="abs band-line" style="left:291px;top:1857px"><b>CUSTOM</b> PROGRAME</p>
<p class="abs band-line" style="left:61px;top:1906px"><b>PROFESSIONAL</b> TRAINING</p>
<p class="abs band-line" style="left:235px;top:1956px"><b>BEST</b> PRICE EVER</p>
<div class="abs band-rule"></div>
<p class="abs band-note">IF YOU WANT TO CHANGE YOUR BODY, YOU FIRST HAVE TO CHANGE YOUR MIND.</p>

<h2 class="abs section-title social-title">Join me on social media</h2>
<p class="abs section-title social-sub">I'm almost everywhere</p>

<a class="abs social" style="left:67px"><span class="social-mark"></span>Pictura</a>
<a class="abs social" style="left:382px"><span class="social-mark"></span>Circlebook</a>
<a class="abs social" style="left:668px"><span class="social-mark"></span>Chirper</a>
<a class="abs social" style="left:970px"><span class="social-mark"></span>Workline</a>

<footer class="abs footer">Copyright Maple Fitness &amp; Health 2014. All Right Reserved</footer>

</body>
</html>
```